Building company requiring web site design

We need a web design for a new company based in Sydney called Harbin Building Co. We build and renovate new and existing homes for consumers. We would like to see design that use the colours red and grey. The final design should communicate innovative building but with old fashion quality, great customer service and attention to detail. I have already had a logo and stationary design completed and would like to use the these colour schemes
Updates

Target Market(s)

Home owners, investors

Industry/Entity Type

Building

Coding

Coded - Design and coding required

Number of Pages Required

5+ page

Requirements
Must have
• Home page, contact page, about us page, gallery page and testimonial page
Nice to have
• Contact form

```html
<!DOCTYPE html>
<html lang="en">
<head>
<meta charset="utf-8">
<title>Harbin Building Co.</title>
<link href="https://fonts.googleapis.com/css2?family=Lato:wght@400;700;900&family=Open+Sans:wght@400;600&display=swap" rel="stylesheet">
<style>
:root{
  --red:#b9454b;
  --red-dark:#a03a40;
  --red-light:#c85a5f;
  --grey-dark:#3a3a3a;
  --footer:#303030;
  --footer-text:#d8d8d8;
  --text:#555;
  --white:#fff;
}
*{margin:0;padding:0;box-sizing:border-box}
html,body{width:1200px;height:2848px;overflow:hidden}
body{position:relative;background:var(--white);font-family:"Open Sans",sans-serif;color:var(--text)}
.abs{position:absolute}
h2{font-family:"Lato",sans-serif;font-weight:700}

/* header */
.logo{left:160px;top:70px;display:flex;align-items:center;gap:16px}
.logo-mark{width:48px;height:48px;background:var(--red)}
.logo-name{font-family:"Lato",sans-serif;font-weight:900;font-size:38px;color:var(--grey-dark);line-height:1}
.contact-top{right:220px;top:96px;text-align:right;font-family:"Lato",sans-serif}
.contact-top .phone{font-size:26px;color:var(--grey-dark);display:flex;align-items:center;gap:10px;justify-content:flex-end}
.contact-top .mail{font-size:15px;color:var(--text);display:flex;align-items:center;gap:8px;justify-content:flex-end;margin-top:8px}

/* nav */
.nav{left:0;top:208px;width:1200px;height:56px;background:var(--red)}
.nav ul{position:absolute;left:160px;top:0;display:flex;list-style:none;height:56px}
.nav li{font-family:"Lato",sans-serif;font-size:18px;color:var(--white);padding:0 18px;line-height:56px}
.nav li.active{background:var(--grey-dark)}
.nav .search{position:absolute;left:990px;top:14px}

/* hero */
.hero{left:0;top:264px;width:1200px;height:528px;background:linear-gradient(180deg,#dfe6ec 0%,#c9d2d9 30%,#8a6a5c 60%,#6f5247 100%)}
.quick{left:704px;top:312px;width:320px;height:410px;background:var(--red);padding:18px 22px}
.quick h3{font-family:"Lato",sans-serif;font-size:30px;font-weight:700;color:var(--white);margin-bottom:18px;line-height:36px}
.quick label{display:block;font-size:13px;color:var(--white);margin-bottom:4px;line-height:18px}
.quick .field{height:30px;background:var(--white);margin-bottom:12px}
.quick .area{height:56px;background:var(--white)}
.quick .submit{float:right;margin-top:12px;background:var(--grey-dark);color:var(--white);font-family:"Lato",sans-serif;font-size:18px;line-height:24px;padding:6px 24px}

/* services */
.service{top:820px;width:272px}
.service .photo{height:160px}
.service h4{font-family:"Lato",sans-serif;font-weight:700;font-size:18px;color:var(--red);text-align:center;margin:28px 0 8px}
.service p{font-size:11px;line-height:15px;text-align:center;padding:0 16px}
.service .more{display:flex;align-items:center;gap:6px;justify-content:center;margin-top:18px;font-size:12px}
.more .btn{background:var(--red);color:var(--white);padding:5px 16px;border-radius:14px;font-family:"Lato",sans-serif}
.more .dot{width:24px;height:24px;border-radius:50%;background:var(--red);display:flex;align-items:center;justify-content:center}

/* welcome */
.welcome{left:0;top:1172px;width:1200px;height:316px;background:var(--red);text-align:center;color:var(--white)}
.welcome h2{font-size:40px;margin-top:38px}
.welcome p{width:880px;margin:22px auto 0;font-size:13px;line-height:19px}
.welcome .more{display:flex;justify-content:center;gap:6px;margin-top:18px}
.welcome .btn{background:var(--white);color:var(--red)}
.welcome .dot{background:var(--white)}

/* gallery */
.gallery-title{left:0;top:1524px;width:1200px;text-align:center}
.gallery-title h2{font-size:38px;color:var(--red)}
.rule{width:120px;height:3px;background:var(--grey-dark);margin:10px auto 0}
.gal{top:1608px;height:212px}
.arrows{left:548px;top:1856px;display:flex;gap:8px}
.arrows span{width:48px;height:36px;background:var(--red);display:flex;align-items:center;justify-content:center}

/* testimonials */
.testi{left:0;top:1920px;width:1200px;height:320px;background:linear-gradient(160deg,var(--red-light),var(--red-dark));text-align:center;color:var(--white)}
.testi h2{font-size:38px;margin-top:24px}
.testi .rule{background:var(--white)}
.avatar{width:92px;height:92px;border-radius:50%;background:#c9b3a6;border:4px solid var(--white);margin:20px auto 0}
.testi h5{font-family:"Lato",sans-serif;font-size:22px;font-weight:700;margin-top:6px}
.testi p{width:880px;margin:10px auto 0;font-size:12px;line-height:17px}
.dots{display:flex;gap:8px;justify-content:center;margin-top:12px}
.dots i{width:9px;height:9px;border-radius:50%;background:rgba(255,255,255,.5)}
.dots i.on{background:var(--white)}

/* newsletter */
.news-label{left:160px;top:2332px;font-family:"Lato",sans-serif;font-size:28px;line-height:38px;color:var(--red);letter-spacing:1px;white-space:nowrap}
.news-input{left:392px;top:2332px;width:408px;height:38px;border:1px solid #ccc;font-size:13px;color:#aaa;padding:10px 12px}
.news-btn{left:812px;top:2332px;width:212px;height:38px;background:var(--red);color:var(--white);font-family:"Lato",sans-serif;font-size:17px;text-align:center;line-height:38px}

/* footer */
.footer{left:0;top:2440px;width:1200px;height:408px;background:var(--footer);text-align:center}
.footer h2{font-size:34px;color:var(--white);font-weight:400;margin-top:18px}
.footer .rule{background:var(--red);width:90px}
.f-field{left:352px;width:228px;height:34px;background:var(--white);font-size:12px;color:#999;text-align:left;padding:9px 10px}
.f-area{left:596px;top:2520px;width:340px;height:130px;background:var(--white);font-size:12px;color:#999;text-align:left;padding:9px 10px}
.f-btns{left:0;top:2666px;width:1200px;display:flex;gap:12px;justify-content:center}
.f-btns span{background:var(--red);color:var(--white);font-size:13px;padding:5px 22px}
.f-info{left:0;top:2710px;width:1200px;font-size:13px;line-height:22px;color:var(--footer-text);display:flex;flex-direction:column;align-items:center}
.f-info div{display:flex;align-items:center;gap:8px}
.social{left:0;top:2800px;width:1200px;display:flex;gap:10px;justify-content:center}
.social i{width:24px;height:24px;border-radius:50%;background:#4a7fc1}
</style>
</head>
<body>

<header>
  <div class="abs logo"><span class="logo-mark"></span><span class="logo-name">Harbin Building Co.</span></div>
  <div class="abs contact-top">
    <div class="phone">
      <svg width="24" height="24" viewBox="0 0 24 24"><circle cx="12" cy="12" r="12" fill="#b9454b"/><path d="M8 6l2 0 1 3-1.5 1a7 7 0 0 0 4 4l1-1.5 3 1 0 2a2 2 0 0 1-2 2A11 11 0 0 1 6 8a2 2 0 0 1 2-2z" fill="#fff"/></svg>
      0140 555 017
    </div>
    <div class="mail">
      <svg width="18" height="18" viewBox="0 0 18 18"><circle cx="9" cy="9" r="9" fill="#b9454b"/><rect x="4" y="5.5" width="10" height="7" fill="#fff"/><path d="M4 5.5l5 4 5-4" stroke="#b9454b" fill="none"/></svg>
      admin@harbinbuildingco.com.au
    </div>
  </div>
</header>

<nav class="abs nav">
  <ul>
    <li class="active">Home</li><li>About Us</li><li>Services</li><li>Gallery</li><li>Testimonials</li><li>Contact Us</li>
  </ul>
  <svg class="search" width="28" height="28" viewBox="0 0 28 28"><circle cx="12" cy="12" r="7" stroke="#fff" stroke-width="3" fill="none"/><path d="M17 17l6 6" stroke="#fff" stroke-width="3"/></svg>
</nav>

<section class="abs hero" role="img" aria-label="Photo of a row of red brick terrace homes under renovation with scaffolding"></section>
<form class="abs quick">
  <h3>Quick Contact</h3>
  <label>Name</label><div class="field"></div>
  <label>Email</label><div class="field"></div>
  <label>Phone</label><div class="field"></div>
  <label>Message</label><div class="area"></div>
  <span class="submit">Submit</span>
</form>

<section class="services">
  <article class="abs service" style="left:160px">
    <div class="photo" role="img" aria-label="Photo of builders in hard hats on site" style="background:linear-gradient(135deg,#c9a76a,#6f7c86)"></div>
    <h4>Construction</h4>
    <p>Quality new homes built with care, from the first footing to the final coat of paint, on time and on budget for every client.</p>
    <div class="more"><span class="btn">Read more</span><span class="dot"><svg width="10" height="10" viewBox="0 0 10 10"><path d="M3 1l4 4-4 4" stroke="#fff" stroke-width="2" fill="none"/></svg></span></div>
  </article>
  <article class="abs service" style="left:464px">
    <div class="photo" role="img" aria-label="Photo of hands using tools for a repair job" style="background:linear-gradient(135deg,#8b6b4c,#d9c3a0)"></div>
    <h4>Repair</h4>
    <p>Fast, reliable repairs for roofs, walls, floors and fittings, handled by skilled trades who treat your home like their own.</p>
    <div class="more"><span class="btn">Read more</span><span class="dot"><svg width="10" height="10" viewBox="0 0 10 10"><path d="M3 1l4 4-4 4" stroke="#fff" stroke-width="2" fill="none"/></svg></span></div>
  </article>
  <article class="abs service" style="left:768px">
    <div class="photo" role="img" aria-label="Photo of a building frame during renovation" style="background:linear-gradient(135deg,#a9c0d6,#8a6a52)"></div>
    <h4>Renovation</h4>
    <p>Thoughtful renovations that bring new life to older homes while keeping the character and craftsmanship of the original build.</p>
    <div class="more"><span class="btn">Read more</span><span class="dot"><svg width="10" height="10" viewBox="0 0 10 10"><path d="M3 1l4 4-4 4" stroke="#fff" stroke-width="2" fill="none"/></svg></span></div>
  </article>
</section>

<section class="abs welcome">
  <h2>Welcome to Harbin Building Co.</h2>
  <p>Harbin Building Co. builds and renovates new and existing homes across Sydney. We bring innovative building methods together with old fashioned quality, so every home we touch is made to last. Our team listens closely, plans carefully and keeps you informed at every stage of the project. From the first meeting to the final handover we focus on great customer service and real attention to detail. Whether you are a home owner planning your dream home or an investor looking for a trusted partner, we deliver honest advice, clear pricing and work you can be proud of for years to come.</p>
  <div class="more"><span class="btn">Read more</span><span class="dot"><svg width="10" height="10" viewBox="0 0 10 10"><path d="M3 1l4 4-4 4" stroke="#b9454b" stroke-width="2" fill="none"/></svg></span></div>
</section>

<div class="abs gallery-title"><h2>Gallery</h2><div class="rule"></div></div>
<div class="abs gal" style="left:160px;width:224px;background:linear-gradient(180deg,#b8c4cc,#7d8a70)" role="img" aria-label="Photo of a modern house exterior"></div>
<div class="abs gal" style="left:384px;width:224px;background:linear-gradient(180deg,#9fb6c8,#6e8a4c)" role="img" aria-label="Photo of a garden path beside a new home"></div>
<div class="abs gal" style="left:608px;width:216px;background:linear-gradient(180deg,#e4e0d8,#8f8a80)" role="img" aria-label="Photo of a bright modern interior"></div>
<div class="abs gal" style="left:824px;width:200px;background:linear-gradient(180deg,#8fb3d8,#7a8e68)" role="img" aria-label="Photo of a multi storey residential building"></div>
<div class="abs arrows">
  <span><svg width="12" height="12" viewBox="0 0 12 12"><path d="M8 1L3 6l5 5" stroke="#fff" stroke-width="2" fill="none"/></svg></span>
  <span><svg width="12" height="12" viewBox="0 0 12 12"><path d="M4 1l5 5-5 5" stroke="#fff" stroke-width="2" fill="none"/></svg></span>
</div>

<section class="abs testi">
  <h2>Testimonials</h2><div class="rule"></div>
  <div class="avatar" role="img" aria-label="Portrait photo of the client"></div>
  <h5>Liam Carter</h5>
  <p>The team at Harbin Building Co. renovated our family home and the result is better than we imagined. They were always on time, kept the site clean and explained every decision clearly. The finish on the timber work and the kitchen shows real care and skill. We would happily recommend them to anyone planning a new build or a renovation in Sydney.</p>
  <div class="dots"><i class="on"></i><i></i><i></i></div>
</section>

<div class="abs news-label">NEWSLETTER</div>
<div class="abs news-input">Your email address</div>
<div class="abs news-btn">Subscribe</div>

<footer class="abs footer">
  <h2>Contact Us</h2><div class="rule"></div>
</footer>
<div class="abs f-field" style="top:2520px">Name</div>
<div class="abs f-field" style="top:2566px">Email</div>
<div class="abs f-field" style="top:2612px">Phone</div>
<div class="abs f-area">Message</div>
<div class="abs f-btns"><span>Clear</span><span>Send</span></div>
<div class="abs f-info">
  <div>88 Harbour Street, Sydney NSW 2000</div>
  <div><svg width="12" height="12" viewBox="0 0 24 24"><path d="M6 3l4 0 1 5-2.5 1.5a10 10 0 0 0 6 6L16 13l5 1 0 4a2 2 0 0 1-2 2A17 17 0 0 1 4 5a2 2 0 0 1 2-2z" fill="#c85a5f"/></svg>0140 555 017</div>
  <div><svg width="12" height="12" viewBox="0 0 12 12"><rect x="1" y="2.5" width="10" height="7" fill="#c85a5f"/><path d="M1 2.5l5 4 5-4" stroke="#303030" fill="none"/></svg>admin@harbinbuildingco.com.au</div>
</div>
<div class="abs social"><i></i><i style="background:#4ab3e8"></i><i style="background:#d04a3c"></i></div>

</body>
</html>
```